Business card design needed

Velvet Moxie is an online boutique for connoisseurs of unique, hand crafted, vintage and pin-up inspired lingerie, delectable handmade lotions & potions and naughty & nice, seduce me please gifts and ideas.

Inspired by vintage glamour, pin-up and burlesque, the site is dedicated to things that make all women look and feel beautiful…with a touch of mischief.

The design should be clean, uncomplicated, sophisticated and in line with the website - See www.velvetmoxie.com.au.

Predominantly black, red and grey in colour.

Font used on the website is Honeyscript and Drescher Grotesk Light

Industry/Entity Type

Boutique

Contact Information for Business Card

Velvet Moxie
Corinne Walsby - Director
0417 639 204
corinne@velvetmoxie.com.au

Requirements
Should not have
• No lace, nothing to girly.

```html
<!DOCTYPE html>
<html lang="en">
<head>
<meta charset="utf-8">
<title>Velvet Moxie — Business Card</title>
<link rel="stylesheet" href="https://fonts.googleapis.com/css2?family=Jost:wght@400&family=Marcellus&display=swap">
<style>
  :root {
    --backdrop: #e8e3dd;
    --card-deep: #3d0709;
    --card-mid: #6b1418;
    --card-glow: #9a2a2e;
    --ink: #ffffff;
    --ink-soft: #f1dede;
  }
  * { box-sizing: border-box; margin: 0; padding: 0; }
  html, body {
    width: 1200px;
    height: 800px;
    overflow: hidden;
    background: var(--backdrop);
  }
  .canvas {
    width: 1200px;
    height: 800px;
    display: flex;
    align-items: center;
    justify-content: center;
    gap: 80px;
  }
  .card {
    position: relative;
    width: 350px;
    height: 574px;
    border-radius: 3px;
    overflow: hidden;
    box-shadow: 0 14px 30px rgba(40, 10, 10, 0.28);
    color: var(--ink);
  }
  .card__pattern {
    position: absolute;
    inset: 0;
    background:
      radial-gradient(ellipse 70% 55% at 50% 48%, var(--card-glow) 0%, var(--card-mid) 45%, var(--card-deep) 100%);
  }
  .card__content {
    position: relative;
    height: 100%;
    display: flex;
    flex-direction: column;
    align-items: center;
  }

  /* Contact side */
  .card--contact .card__content { padding-top: 92px; }
  .brand {
    display: flex;
    flex-direction: column;
    align-items: center;
    gap: 16px;
  }
  .brand__dot {
    width: 44px;
    height: 44px;
    border-radius: 50%;
    background: var(--ink);
  }
  .brand__name {
    font-family: "Marcellus", serif;
    font-size: 19px;
    letter-spacing: 4px;
    text-transform: uppercase;
    color: var(--ink-soft);
  }
  .person {
    margin-top: 96px;
    text-align: center;
  }
  .person__name {
    font-family: "Marcellus", serif;
    font-size: 27px;
    letter-spacing: 1.5px;
    text-transform: uppercase;
    font-weight: 400;
  }
  .person__role {
    font-family: "Jost", sans-serif;
    font-size: 10px;
    letter-spacing: 1.5px;
    text-transform: uppercase;
    margin-top: 2px;
  }
  .contact {
    margin-top: 18px;
    list-style: none;
    font-family: "Jost", sans-serif;
    font-size: 15px;
    line-height: 1.45;
    text-align: left;
  }

  /* Brand side */
  .card--brand .card__content { justify-content: center; gap: 26px; }
  .card--brand .brand__dot { width: 70px; height: 70px; }
  .card--brand .brand__name { font-size: 30px; letter-spacing: 6px; color: var(--ink); }
</style>
</head>
<body>
  <main class="canvas">
    <article class="card card--contact">
      <div class="card__pattern" role="img" aria-label="Dark red damask pattern background"></div>
      <div class="card__content">
        <header class="brand">
          <span class="brand__dot"></span>
          <span class="brand__name">Velvet Moxie</span>
        </header>
        <div class="person">
          <h1 class="person__name">Corinne Walsby</h1>
          <p class="person__role">Director</p>
        </div>
        <ul class="contact">
          <li>P: 0417 639 204</li>
          <li>E: corinne@velvetmoxie.com.au</li>
          <li>www.velvetmoxie.com.au</li>
        </ul>
      </div>
    </article>

    <article class="card card--brand">
      <div class="card__pattern" role="img" aria-label="Dark red damask pattern background"></div>
      <div class="card__content">
        <span class="brand__dot"></span>
        <span class="brand__name">Velvet Moxie</span>
      </div>
    </article>
  </main>
</body>
</html>
```